Investment Funding, Building and Construction

I need a design logo for my new business based out of Houston, TX called Kestrel Ridge Holdings LLC., We are a company looking to help fund and invest into other small/businesses that do not want to deal with the banking system. We also remodel, renovate, and build from the ground up anything from residential, industrial warehousing, and commercial buildings. We would like the design to express our great deal of passion that we have for the work, our dedication to helping the costumer/businesses receive their expectation of work and also our professionalism and commitment to making sure we get the job done as perfect as possible. We want to build your future!

Target Market(s)

Architects, Design Companies, Home Owners and Real Estate

Industry/Entity Type

Construction Company

Contact Information for Business Card

Name: Dorian Pellham
Position: CEO/President
Company Name: Kestrel Ridge Holdings LLC.,
Website: www.kestrelridgehold.example
Phone: 281-507-3619
Email: kestrelridgehold@mailbox.example, crewfundflow@mailbox.example

Font styles to use
Serif

Colors
f04a50
3377b5

Requirements
Must have
• Motivational, Inspiring, and Detailed oriented work but simple.
Nice to have
• I would like to see excitement and enthusiasm within the card.
Should not have
• The project can not be boring and lack of detail.

```html
<!DOCTYPE html>
<html lang="en">
<head>
<meta charset="utf-8">
<title>Kestrel Ridge Holdings LLC – Business Card</title>
<link rel="stylesheet" href="https://fonts.googleapis.com/css2?family=Cormorant+Garamond:wght@500;600&display=swap">
<style>
  :root {
    --card-bg: #060708;
    --ink: #ffffff;
    --ink-soft: #e6e9ee;
    --accent-red: #f04a50;
    --accent-blue: #3377b5;
    --glow: rgba(255,255,255,0.45);
    --crop: #3a3a3a;
  }
  html, body {
    margin: 0;
    padding: 0;
    width: 1200px;
    height: 720px;
    overflow: hidden;
    background: var(--card-bg);
  }
  .card {
    position: relative;
    width: 1200px;
    height: 720px;
    overflow: hidden;
    background: var(--card-bg);
    font-family: "Cormorant Garamond", Georgia, serif;
    color: var(--ink);
  }
  .sweep-art,
  .crop-marks {
    position: absolute;
    inset: 0;
    width: 1200px;
    height: 720px;
  }
  .company-name {
    position: absolute;
    left: 42px;
    top: 200px;
    margin: 0;
    white-space: nowrap;
    font-weight: 600;
    text-transform: uppercase;
    line-height: 1;
    text-shadow: 0 0 8px var(--glow);
  }
  .company-name .lead-word {
    font-size: 74px;
    letter-spacing: -0.5px;
    margin-right: 20px;
    color: var(--accent-red);
    text-shadow: none;
  }
  .company-name .rest {
    font-size: 46px;
    letter-spacing: 0;
  }
  .holder {
    position: absolute;
    right: 22px;
    top: 138px;
    width: 320px;
    text-align: center;
  }
  .holder-name {
    margin: 0;
    font-size: 42px;
    font-weight: 600;
    text-transform: uppercase;
    line-height: 1;
    padding-bottom: 6px;
    border-bottom: 2px solid var(--accent-red);
    text-shadow: 0 0 6px var(--glow);
  }
  .holder-title {
    margin: 12px 0 0;
    font-size: 27px;
    font-weight: 600;
    text-transform: uppercase;
    color: var(--ink-soft);
  }
  .contact-list {
    position: absolute;
    left: 114px;
    top: 405px;
    margin: 0;
    padding: 0;
    list-style: none;
  }
  .contact-item {
    position: relative;
    padding-left: 72px;
    min-height: 40px;
  }
  .contact-icon {
    position: absolute;
    left: 0;
    top: 0;
    width: 38px;
    height: 38px;
  }
  .contact-phone {
    font-size: 26px;
    font-weight: 600;
    line-height: 40px;
    margin-bottom: 22px;
  }
  .contact-email,
  .contact-web {
    font-size: 23px;
    font-weight: 600;
    font-variant: small-caps;
    text-transform: lowercase;
    letter-spacing: 3px;
    color: var(--ink-soft);
  }
  .contact-email { line-height: 46px; margin-bottom: 8px; }
  .contact-email .contact-icon { top: 18px; }
  .contact-web { line-height: 40px; }
</style>
</head>
<body>
<main class="card">
  <svg class="sweep-art" viewBox="0 0 1200 720" role="img" aria-label="Curved light sweep artwork">
    <defs>
      <linearGradient id="sweep-fill" x1="0" y1="0" x2="0.4" y2="1">
        <stop offset="0" stop-color="#3377b5" stop-opacity="0.85"/>
        <stop offset="1" stop-color="#15243a" stop-opacity="0.9"/>
      </linearGradient>
    </defs>
    <path d="M606 0 Q 850 250 826 720 L 1010 720 Q 960 260 640 0 Z" fill="url(#sweep-fill)"/>
  </svg>

  <svg class="crop-marks" viewBox="0 0 1200 720" aria-hidden="true" stroke="var(--crop)" stroke-width="1">
    <path d="M0 39 H18 M39 0 V18 M1182 39 H1200 M1161 0 V18 M0 681 H18 M39 702 V720 M1182 681 H1200 M1161 702 V720"/>
  </svg>

  <h1 class="company-name"><span class="lead-word">Kestrel</span><span class="rest">Ridge Holdings LLC</span></h1>

  <section class="holder">
    <h2 class="holder-name">Dorian Pellham</h2>
    <p class="holder-title">CEO/ President</p>
  </section>

  <ul class="contact-list">
    <li class="contact-item contact-phone">
      <svg class="contact-icon" viewBox="0 0 40 40" aria-hidden="true">
        <path fill="var(--accent-blue)" d="M10 3 C7 3 4 6 4 10 C5 24 16 35 30 36 C34 36 37 33 37 30 L37 27 C37 26 36 25 35 25 L28 23 C27 23 26 23 25 24 L22 27 C17 25 15 23 13 18 L16 15 C17 14 17 13 17 12 L15 5 C15 4 14 3 13 3 Z"/>
      </svg>
      281-507-3619
    </li>
    <li class="contact-item contact-email">
      <svg class="contact-icon" viewBox="0 0 40 40" aria-hidden="true">
        <rect x="3" y="8" width="32" height="24" fill="var(--accent-blue)"/>
        <path d="M3 8 L19 22 L35 8 M3 32 L15 19 M35 32 L23 19" fill="none" stroke="#060708" stroke-width="2"/>
      </svg>
      crewfundflow@mailbox.example<br>
      kestrelridgehold@mailbox.example
    </li>
    <li class="contact-item contact-web">
      <svg class="contact-icon" viewBox="0 0 40 40" aria-hidden="true">
        <circle cx="20" cy="20" r="16" fill="var(--accent-blue)"/>
        <path d="M4 20 H36 M20 4 V36" fill="none" stroke="#060708" stroke-width="2.5"/>
        <ellipse cx="20" cy="20" rx="7" ry="16" fill="none" stroke="#060708" stroke-width="2"/>
      </svg>
      www.kestrelridgehold.example
    </li>
  </ul>
</main>
</body>
</html>
```